Lawn & Garden Maintenace Business card design needed

I need a basic business card design for a Lawn Mowing & Garden Maintenance business

I would like it to look a combination of classy, striking, with vibrant Green/s, I will attached a very rough idea of what I would like but I am open to new suggestions, and the possibility of doing it on a darker charcoal or black gloss card, please don't just send me a version of what I've attached it's a very rough idea & more based around the text layout than anything else, feel free to let your creative instincts fly!

Must have grass across the bottom of the Card & i would prefer it to be portrait rather than landscape.

I quite like the coloring of this previously submitted card
http://www.artspark-example.com/design/2840613

Please have the text in White and Green if you are submitting a dark card, thank you.

Business

R.K. Lawn & Garden Services

Free Quote - Great Rates

Rob Kessler
0417 362 918
Info@RKLawnAndGarden.example.au

Requirements
Must have
• Must have grass across bottom of card preferably photo real grass rather than illustrated.
Nice to have
• Small telephone icon for phone number small email icon for email address but only if both icon are similar size and don't take away from the overall look of the card

Would also be nice to a have a flow/style that would be easily transferable to flyers & advertising

```html
<!DOCTYPE html>
<html lang="en">
<head>
<meta charset="utf-8">
<title>R.K. Lawn &amp; Garden Services – Business Card</title>
<link href="https://fonts.googleapis.com/css2?family=Cinzel:wght@400&family=Open+Sans:wght@400&display=swap" rel="stylesheet">
<style>
  :root {
    --page-bg: #d9d9d9;
    --card-black: #050505;
    --text-white: #ffffff;
    --brand-green: #5cb531;
    --grass-light: #7fd23a;
    --grass-mid: #3f9a1f;
    --grass-dark: #1d5a12;
    --turf-light: #3c8d2c;
    --turf-dark: #16491a;
  }
  * { box-sizing: border-box; margin: 0; padding: 0; }
  html, body { width: 1200px; height: 960px; overflow: hidden; }
  body {
    background: var(--page-bg);
    display: flex;
    flex-direction: column;
    align-items: center;
    justify-content: center;
    gap: 40px;
  }
  .card {
    position: relative;
    width: 760px;
    height: 434px;
    overflow: hidden;
    box-shadow: 0 10px 30px rgba(0,0,0,0.25);
  }

  /* Front */
  .card-front {
    background: var(--card-black);
    border-radius: 0 0 120px 0;
  }
  .tagline {
    position: absolute;
    left: 48px; top: 118px;
    font-family: "Cinzel", serif;
    font-size: 27px;
    color: var(--brand-green);
    letter-spacing: 0.5px;
  }
  .contact {
    position: absolute;
    left: 70px; top: 178px;
    font-family: "Open Sans", sans-serif;
    color: var(--text-white);
  }
  .contact-name { font-size: 40px; line-height: 1.1; margin-bottom: 14px; }
  .contact-line {
    display: flex; align-items: center; gap: 12px;
    font-size: 22px; line-height: 1.6;
  }
  .contact-icon {
    width: 22px; height: 22px;
    background: var(--brand-green);
    color: var(--text-white);
    font-size: 13px;
    display: flex; align-items: center; justify-content: center;
  }
  .brand-name {
    position: absolute;
    font-family: "Cinzel", serif;
    font-weight: 400;
    color: var(--text-white);
    text-align: center;
    line-height: 1.3;
  }
  .card-front .brand-name {
    right: 44px; top: 100px;
    width: 220px;
    font-size: 22px;
  }
  .grass-band { position: absolute; left: 0; bottom: 0; width: 760px; height: 140px; }

  /* Back */
  .card-back { border-radius: 0 0 0 120px; }
  .turf { position: absolute; inset: 0; width: 100%; height: 100%; }
  .card-back .brand-name {
    left: 0; right: 0; top: 150px;
    font-size: 34px;
  }
  .services {
    position: absolute;
    left: 0; right: 0; top: 260px;
    font-family: "Cinzel", serif;
    color: var(--text-white);
    text-align: center;
    font-size: 22px;
    line-height: 1.4;
    letter-spacing: 1px;
  }
</style>
</head>
<body>

  <section class="card card-front">
    <p class="tagline">Free Quote - Great Rates</p>
    <div class="contact">
      <p class="contact-name">Rob Kessler</p>
      <p class="contact-line"><span class="contact-icon">M</span>0417 362 918</p>
      <p class="contact-line"><span class="contact-icon">E</span>Rob@rklawnandgarden.example.au</p>
    </div>
    <p class="brand-name">R.K. Lawn &amp; Garden Services</p>
    <svg class="grass-band" viewBox="0 0 760 140" role="img" aria-label="Photo-real green grass growing across the bottom of the card">
      <defs>
        <linearGradient id="grassFade" x1="0" y1="0" x2="0" y2="1">
          <stop offset="0" stop-color="var(--grass-light)"/>
          <stop offset="0.55" stop-color="var(--grass-mid)"/>
          <stop offset="1" stop-color="var(--grass-dark)"/>
        </linearGradient>
      </defs>
      <path d="M0 110 C150 100 300 90 420 70 C560 50 660 35 760 20 L760 140 L0 140 Z" fill="url(#grassFade)"/>
    </svg>
  </section>

  <section class="card card-back">
    <svg class="turf" viewBox="0 0 760 434" preserveAspectRatio="none" role="img" aria-label="Close-up photo of a green lawn covering the card">
      <defs>
        <radialGradient id="turfGlow" cx="0.6" cy="0.3" r="0.8">
          <stop offset="0" stop-color="var(--turf-light)"/>
          <stop offset="1" stop-color="var(--turf-dark)"/>
        </radialGradient>
      </defs>
      <rect width="760" height="434" fill="url(#turfGlow)"/>
    </svg>
    <p class="brand-name">R.K. Lawn &amp; Garden Services</p>
    <p class="services">Mowing - Edging - Pruning - Weeding<br>Planting &amp; More</p>
  </section>

</body>
</html>
```